Letterhead for a German Distribution/Manufacturing Company

We need a professional Letterhead in a unique Design.
not to playful.
The Letterhead has to show show that we are a international company with headquater in Germany.
all details like adress, Vat Tax Number, Bank Accout, Eori, email, Company number has to be on the Letterhead.
for example use: VAT TAX DE5704168 Bank Account: Norrfeld Bank IBAN DE421705238ß310482 Swift: KOLV3154802 EORI 3041296587 Company Number: HRB 61508 Adress: VOLTRINA UG Amsel Strasse 7 Postal Code 04683 City Burgstädt Country: Germany Email: info@voltrina-example.com
the design can be colored but doesnt have to be
Industry/Entity Type
Manufacturing and international distribution
Requirements
Must have
- show that we are a international company with headquater in Germany. our company infos and logo

```html
<!DOCTYPE html>
<html lang="en">
<head>
<meta charset="utf-8">
<title>VOLTRINA Letterhead</title>
<link rel="stylesheet" href="https://fonts.googleapis.com/css2?family=Poppins:wght@400;500;600&family=Merriweather:wght@700&display=swap">
<style>
  :root {
    --bg: #e1e2e3;
    --paper: #ffffff;
    --band-dark: #484848;
    --band-light: #585858;
    --on-band: #ffffff;
    --ink: #222222;
    --body: #3c3c3c;
    --muted: #7a7a7a;
    --rule: #2e2e2e;
  }
  * { box-sizing: border-box; margin: 0; padding: 0; }
  html, body { width: 961px; height: 1200px; overflow: hidden; background: var(--bg); }
  body { font-family: "Poppins", sans-serif; position: relative; }
  .sheet {
    position: absolute; left: 52px; top: 0; width: 856px; height: 1200px;
    background: var(--paper);
  }
  .masthead {
    position: absolute; left: 0; top: 0; width: 856px; height: 141px;
    background: linear-gradient(90deg, var(--band-dark), var(--band-light) 40%, var(--band-light));
    color: var(--on-band);
  }
  .brand {
    position: absolute; left: 29px; top: 44px; display: flex; align-items: center; gap: 12px;
    font-size: 40px; font-weight: 400; letter-spacing: 0.5px; line-height: 1;
  }
  .brand-dot { width: 40px; height: 40px; border-radius: 50%; background: var(--on-band); flex: none; }
  .contact, .hq { position: absolute; top: 51px; font-size: 12px; line-height: 18.5px; white-space: nowrap; }
  .contact { left: 418px; }
  .divider { position: absolute; left: 612px; top: 36px; width: 1px; height: 88px; background: rgba(255,255,255,0.55); }
  .hq { left: 640px; }
  .recipient { position: absolute; left: 29px; top: 238px; color: var(--ink); }
  .recipient .to { font-size: 12.5px; line-height: 14px; color: var(--body); }
  .recipient .name { font-size: 19.5px; font-weight: 600; line-height: 22px; }
  .recipient .role { font-family: "Merriweather", serif; font-weight: 700; font-size: 13.5px; line-height: 21px; }
  .recipient .address { font-size: 13.6px; line-height: 20px; color: var(--muted); margin-top: 3px; }
  .date { position: absolute; right: 38px; top: 238px; font-size: 12px; font-weight: 500; color: var(--body); line-height: 14px; }
  .letter-body { position: absolute; left: 29px; top: 440px; width: 796px; color: var(--body); font-size: 12.4px; line-height: 22.4px; letter-spacing: 0.08px; text-align: justify; }
  .letter-body p + p { margin-top: 25px; }
  .sign-off { position: absolute; left: 29px; top: 900px; width: 194px; }
  .signature-mark { display: block; margin-left: 22px; width: 120px; height: 38px; background: linear-gradient(90deg, #f3f3f3, #e6e6e6); }
  .sign-rule { height: 1px; background: var(--rule); margin-top: 13px; }
  .sign-label { text-align: center; font-size: 10px; font-weight: 600; letter-spacing: 6.5px; color: var(--body); margin-top: 9px; padding-left: 6px; }
  .footer-band { position: absolute; left: 0; top: 1107px; width: 856px; height: 64px; color: var(--on-band); }
  .footer-band svg { position: absolute; inset: 0; }
  .footer-item { position: absolute; top: 13px; line-height: 15px; white-space: nowrap; }
  .footer-item .label { font-weight: 600; }
  .company-number { left: 29px; font-size: 13.6px; line-height: 16px; }
  .vat { left: 240px; font-size: 12px; }
  .bank { left: 426px; font-size: 11.8px; }
  .bank b { font-weight: 600; }
</style>
</head>
<body>
  <main class="sheet">
    <header class="masthead">
      <div class="brand"><span class="brand-dot"></span><span class="brand-name">VOLTRINA</span></div>
      <div class="contact">12 3456 0417<br>info@voltrina-example.com<br>www.voltrina-example.com</div>
      <div class="divider"></div>
      <div class="hq">VOLTRINA UG Amsel Strasse 7<br>Postal Code 04683, Burgstädt<br>Germany</div>
    </header>

    <section class="recipient">
      <div class="to">To</div>
      <div class="name">Jonas Keller</div>
      <div class="role">CEO, Brightmoor Studio</div>
      <div class="address">3307 Alder Ridge Rd S204<br>Lakeview, WA 98110</div>
    </section>
    <div class="date">Date: 07-09-2022</div>

    <article class="letter-body">
      <p>Lorem ipsum dolor sit amet, consectetuer adipiscing elit, sed diam nonummy nibh euismod tincidunt ut laoreet dolore magna aliquam erat volutpat. Ut wisi enim ad minim veniam, quis nostrud exerci tation ullamcorper suscipit lobortis nisl ut aliquip ex ea commodo consequat.</p>
      <p>Lorem ipsum dolor sit amet, cons ectetuer adipiscing elit, sed diam nonummy nibh euismod tincidunt ut laoreet dolore magna aliquam erat volutpat. Ut wisi enim ad minim veniam, quis nostrud exerci tation ullamcorper suscipit lobortis nisl ut aliquip ex ea commodo consequat.</p>
      <p>Lorem ipsum dolor sit amet, consectetuer adipiscing elit, sed diam nonummy nibh euismod tincidunt ut laoreet dolore magna aliquam erat volutpat. Ut wisi enim ad minim veniam, quis nostrud exerci tation ullamcorper suscipit lobortis nisl ut aliquip ex ea commodo consequat.</p>
      <p>Lorem ipsum dolor sit amet, consectetuer adipiscing elit, sed diam nonummy nibh euismod tincidunt ut laoreet dolore magna aliquam erat volutpat. Ut wisi enim ad minim veniam, quis nostrud exerci tation ullamcorper suscipit lobortis nisl ut aliquip ex ea commodo consequat. Duis autem vel eum iriure dolor in hendrerit in vulputate velit esse molestie consequat, vel illum dolore eu feugiat nulla facilisis at vero eros et accumsan et iusto odio dignissim qui blandit praesent luptatum zzril delenit augue duis dolore te feugait nulla facilisi.</p>
    </article>

    <section class="sign-off">
      <span class="signature-mark" role="img" aria-label="Handwritten signature"></span>
      <div class="sign-rule"></div>
      <div class="sign-label">SIGNATURE</div>
    </section>

    <footer class="footer-band">
      <svg width="856" height="64" viewBox="0 0 856 64" aria-hidden="true">
        <polygon points="0,0 213,0 167,64 0,64" fill="#4a4a4a"/>
        <polygon points="230,0 394,0 348,64 184,64" fill="#4f4f4f"/>
        <polygon points="411,0 856,0 856,64 365,64" fill="#575757"/>
      </svg>
      <div class="footer-item company-number"><div class="label">Company Number</div><div>HRB 61508</div></div>
      <div class="footer-item vat"><div class="label">VAT TAX</div><div>DE5704168</div></div>
      <div class="footer-item bank"><div class="label">Bank Account : Norrfeld Bank</div><div><b>IBAN</b> DE421705238ß310482 <b>Swift:</b> KOLV3154802 <b>EORI</b> 3041296587</div></div>
    </footer>
  </main>
</body>
</html>
```